Gaphic explaining connectivity of research areas that use DNA analysis

We are a university research group in Perth Western Australia focused on ecology and environment fields. Our work can be explained by three broad areas where its applied - what used to be present ('ancient DNA analysis'), what is present now ('environmental DNA analysis') and what happened in terms of DNA based changes in between ('genomic changes'). To help simply convey this to other researchers and importantly non-science-savvy people we wanted an a eye catching rework of the attached for our website, future presentations, brochures etc. We didn't want it too visually complicated, nor wordy so something akin to the attached with a better look will help . More background on each point can be read on the website under construction here - https://sciweb.halvorne.edu.au/quill-lab/

Target Market(s)

other science researchers in ecology, environment, geology, forensics areas, although ultimately its meant to be a simple way to understand for all people

Font styles to use
Sans Serif

Requirements
Must have
• the three areas indicated
Should not have
• design does not need to follow the colour pallet of the university (ie poo brown and black)

```html
<!DOCTYPE html>
<html lang="en">
<head>
<meta charset="utf-8">
<title>Connectivity of research areas that use DNA analysis</title>
<link rel="stylesheet" href="https://fonts.googleapis.com/css2?family=Montserrat:wght@500;600;700&display=swap">
<style>
  :root {
    --steel: #5489a6;
    --sky: #7bbbd4;
    --navy: #023350;
    --ink: #1d1d1d;
    --track: #d3d2d2;
    --halo: #f4f4f3;
    --disc: #e4e4e4;
    --paper: #ffffff;
  }
  * { margin: 0; padding: 0; box-sizing: border-box; }
  html, body { width: 1200px; height: 800px; overflow: hidden; background: var(--paper); }
  body { font-family: "Montserrat", Arial, sans-serif; }
  .canvas { position: relative; width: 1200px; height: 800px; overflow: hidden; }
  .backdrop { position: absolute; inset: 0; }
  .title {
    position: absolute; left: 0; right: 0; top: 26px;
    text-align: center; color: var(--paper); white-space: nowrap;
    font-weight: 700; font-size: 20px; line-height: 27px;
    letter-spacing: 0.29em; padding-left: 0.29em;
  }
  .area-bar {
    position: absolute; left: 229px; top: 427px; width: 742px; height: 39px;
    display: flex; border-radius: 20px; overflow: hidden;
  }
  .area-bar span {
    display: flex; align-items: center; justify-content: center;
    color: var(--paper); font-weight: 500; font-size: 20px;
    letter-spacing: 0.33em; padding-left: 0.33em;
  }
  .area-adna { width: 239px; background: var(--sky); }
  .area-genomic { width: 263px; background: var(--steel); }
  .area-edna { width: 240px; background: var(--navy); }
  .question {
    position: absolute; top: 472px; width: 320px;
    text-align: center; white-space: nowrap;
    font-weight: 600; font-size: 20px; line-height: 27px;
    letter-spacing: 0.26em; padding-left: 0.26em;
  }
  .q-past { left: 188px; color: var(--sky); }
  .q-between { left: 440px; color: var(--steel); }
  .q-now { left: 691px; color: var(--navy); }
  .insight {
    position: absolute; left: 0; right: 0; top: 618px;
    text-align: center; color: var(--ink); white-space: nowrap;
    font-weight: 700; font-size: 18px; line-height: 25px;
    letter-spacing: 0.27em; padding-left: 0.27em;
  }
  .brand {
    position: absolute; left: 880px; top: 742px;
    display: flex; align-items: center; gap: 12px;
    color: var(--paper); font-weight: 500; font-size: 24px;
  }
  .brand-mark { width: 34px; height: 34px; background: var(--paper); }
</style>
</head>
<body>
<div class="canvas">
  <svg class="backdrop" width="1200" height="800" viewBox="0 0 1200 800">
    <ellipse cx="597" cy="-40" rx="352" ry="196" fill="var(--steel)"/>
    <ellipse cx="1015" cy="900" rx="400" ry="186" fill="var(--steel)"/>

    <path d="M252 292 A96 96 0 0 0 444 292 A29.5 29.5 0 0 1 503 292 A96 96 0 0 0 696 292 A29.5 29.5 0 0 1 755 292 A96 96 0 0 0 948 292"
          fill="none" stroke="var(--track)" stroke-width="2.5"/>
    <circle cx="252" cy="292" r="3.5" fill="var(--track)"/>
    <circle cx="948" cy="292" r="3.5" fill="var(--track)"/>

    <g class="area-node">
      <circle cx="348" cy="289" r="86" fill="var(--halo)"/>
      <circle cx="348" cy="289" r="72" fill="var(--disc)" role="img" aria-label="Icon: DNA strand under a magnifying glass"/>
      <line x1="348" y1="386" x2="348" y2="427" stroke="var(--track)" stroke-width="2.5"/>
    </g>
    <g class="area-node">
      <circle cx="600" cy="289" r="86" fill="var(--halo)"/>
      <circle cx="600" cy="289" r="72" fill="var(--disc)" role="img" aria-label="Icon: two DNA strands exchanging, with arrows between"/>
      <line x1="600" y1="386" x2="600" y2="427" stroke="var(--track)" stroke-width="2.5"/>
    </g>
    <g class="area-node">
      <circle cx="851" cy="289" r="86" fill="var(--halo)"/>
      <circle cx="851" cy="289" r="72" fill="var(--disc)" role="img" aria-label="Icon: DNA strand circled by refresh arrows"/>
      <line x1="851" y1="386" x2="851" y2="427" stroke="var(--track)" stroke-width="2.5"/>
    </g>

    <line x1="348" y1="534" x2="348" y2="600" stroke="var(--sky)" stroke-width="2"/>
    <line x1="600" y1="534" x2="600" y2="600" stroke="var(--steel)" stroke-width="2"/>
    <line x1="851" y1="534" x2="851" y2="600" stroke="var(--navy)" stroke-width="2"/>
  </svg>

  <h1 class="title">CONNECTIVITY OF RESEARCH AREAS<br>THAT USE DNA ANALYSIS</h1>

  <div class="area-bar">
    <span class="area-adna">aDNA</span>
    <span class="area-genomic">GENOMIC</span>
    <span class="area-edna">eDNA</span>
  </div>

  <p class="question q-past">What used to<br>be present?</p>
  <p class="question q-between">What happened<br>along the way?</p>
  <p class="question q-now">What is<br>present?</p>

  <p class="insight">INSIGHT ON THE FORMATION, DISTRIBUTION, AND RESILIENCE<br>OF AUSTRALIAN BIODIVERSITY</p>

  <div class="brand">
    <span class="brand-mark"></span>
    <span class="brand-name">Halvorne University</span>
  </div>
</div>
</body>
</html>
```